Oil and Gas Exploration and Production company needs a business card design

We need a business card design using our logo and colors in the logo. We want a mainstream design.

```html
<!DOCTYPE html>
<html lang="en">
<head>
<meta charset="utf-8">
<title>Solvara Energy Business Card</title>
<link href="https://fonts.googleapis.com/css2?family=Source+Sans+3:wght@400;600;700&display=swap" rel="stylesheet">
<style>
  :root {
    --gold: #cf9d31;
    --gold-light: #e9d44c;
    --gold-deep: #c48f2c;
    --ink: #2b2121;
    --black: #111111;
    --paper: #f7f7f5;
    --white: #ffffff;
    --backdrop: #3a3a3a;
  }
  * { margin: 0; padding: 0; box-sizing: border-box; }
  html, body {
    width: 1200px; height: 900px; overflow: hidden;
    background: var(--backdrop);
    font-family: "Source Sans 3", "Helvetica Neue", Arial, sans-serif;
  }
  .canvas {
    position: relative; width: 1200px; height: 900px;
  }
  .card {
    position: absolute; left: 280px; width: 640px; height: 366px;
    overflow: hidden; box-shadow: 0 12px 30px rgba(0,0,0,.45);
  }

  /* Back side */
  .card-back {
    top: 54px;
    background: linear-gradient(100deg, var(--gold-light) 0%, var(--gold) 55%, var(--gold-deep) 100%);
  }
  .card-back .brand {
    position: absolute; left: 0; right: 0; top: 138px;
    display: flex; justify-content: center; align-items: center; gap: 14px;
  }
  .brand-dot {
    width: 22px; height: 22px; border-radius: 50%; background: var(--ink);
  }
  .card-back .brand-name {
    font-size: 54px; font-weight: 700; color: var(--ink); letter-spacing: 1px; line-height: 1;
  }
  .card-back .website {
    position: absolute; right: 40px; bottom: 30px;
    color: var(--white); font-size: 15px; letter-spacing: 5px;
  }

  /* Front side */
  .card-front {
    top: 480px; background: var(--paper);
  }
  .card-front .bands { position: absolute; inset: 0; }
  .card-front .brand {
    position: absolute; left: 150px; top: 80px;
    display: flex; align-items: center; gap: 12px;
  }
  .card-front .brand-dot { width: 18px; height: 18px; }
  .card-front .brand-name {
    font-size: 46px; font-weight: 700; color: var(--ink); line-height: 1;
  }
  .contact-list {
    position: absolute; right: 18px; top: 146px;
    list-style: none; text-align: right;
    color: var(--white); font-size: 14.5px; line-height: 19px;
  }
  .contact-list li { display: flex; justify-content: flex-end; align-items: center; gap: 8px; }
  .contact-list svg { width: 12px; height: 12px; fill: var(--black); }
  .contact-list .email { margin-right: 20px; }
  .person {
    position: absolute; left: 38px; top: 238px; color: var(--white);
  }
  .person-name {
    color: var(--gold); font-weight: 700; font-size: 20px; letter-spacing: .5px; line-height: 1.1;
  }
  .person-title { font-size: 14px; letter-spacing: .5px; margin-bottom: 4px; }
  .person-address { font-size: 15px; line-height: 19px; font-style: normal; }
</style>
</head>
<body>
<main class="canvas">

  <section class="card card-back" aria-label="Business card back">
    <div class="brand">
      <span class="brand-dot"></span>
      <span class="brand-name">Solvara Energy</span>
    </div>
    <p class="website">www.solvaraenergy.com</p>
  </section>

  <section class="card card-front" aria-label="Business card front">
    <svg class="bands" viewBox="0 0 640 366" preserveAspectRatio="none" aria-hidden="true">
      <rect x="330" y="132" width="310" height="130" fill="var(--gold)"/>
      <path d="M0 214 H370 Q400 214 410 240 L440 318 H0 Z" fill="var(--black)"/>
    </svg>

    <div class="brand">
      <span class="brand-dot"></span>
      <span class="brand-name">Solvara Energy</span>
    </div>

    <ul class="contact-list">
      <li>555 0142 7781
        <svg viewBox="0 0 12 12"><path d="M2.5 1 4.5 3 3.6 4.4a7 7 0 0 0 4 4L9 7.5l2 2-1.3 1.5C5.5 11 1 6.5 1 2.3Z"/></svg>
      </li>
      <li>555 0198 3364
        <svg viewBox="0 0 12 12"><path d="M3 0h6v12H3Zm1 1.5v8h4v-8Z"/></svg>
      </li>
      <li>555 0127 4509
        <svg viewBox="0 0 12 12"><path d="M3 0h6v3H3ZM0 4h12v6H9v2H3v-2H0Zm4 5v2h4V9Z"/></svg>
      </li>
      <li class="email-row">info@solvaraenergy.com
        <svg viewBox="0 0 12 12"><path d="M0 2h12v8H0Zm1 1 5 4 5-4Z" fill-rule="evenodd"/></svg>
      </li>
    </ul>

    <div class="person">
      <p class="person-name">MARA QUELL</p>
      <p class="person-title">PRESIDENT</p>
      <address class="person-address">2207 Harlow Lane<br>Cedar Bend, NY 11020</address>
    </div>
  </section>

</main>
</body>
</html>
```